Wedding Invitation and Logo

We would like an invitation and logo designed for our wedding on October 19, 2019 in Charlotte, NC. Our names are Mara and Cobb, we met in school at Brindlemoor Valley College, and we got engaged at a fire tower which has a view down to the campus. You do not have to include these, but some ideas for the invitation design would be mountains, a fire tower, our initials, or the city. The wedding will be at 4:30 in the afternoon with a reception to follow. We do not need to list the families as there are four of them and that is too much info. The colors we would like to use are white, black, royal blue, and maybe silver. Do not feel obligated to use them all though.We would like the logo to include similar elements such as mountains, fire tower, or our initials(M and C). The logo can be a one color design as we may use it on our cake, as light filters to be displayed on the walls at our reception, or as an accent on name plates and stationery.We like simple, clean designs and our wedding will have a wintery theme (white linens, white chair covers, silver and royal blue accents, etc.).Things we do not want: snowflakes, flowers, polka dots, leaves, gold foil.Thank you!

Font styles to use
Serif
Script

Requirements
Must have
• Some combination of white, black, royal blue, optionally silver.
Nice to have
• Mountains, fire tower, our initials (M and C), wintry theme (no snowflakes)
Should not have
• Snowflakes, flowers, polka dots, leaves, gold foil

```html
<!DOCTYPE html>
<html lang="en">
<head>
<meta charset="utf-8">
<title>Mara &amp; Cobb — Wedding Invitation and Logo Card</title>
<link href="https://fonts.googleapis.com/css2?family=Playfair+Display:wght@400;500&family=Montserrat:wght@400&family=Bebas+Neue&display=swap" rel="stylesheet">
<style>
  :root {
    --ground: #ece7dc;
    --paper: #ffffff;
    --ink: #1f2048;
    --royal: #0a27b5;
    --white: #ffffff;
  }
  html, body {
    margin: 0;
    padding: 0;
    width: 1200px;
    height: 1200px;
    overflow: hidden;
    background: var(--ground);
  }
  .canvas {
    position: relative;
    width: 1200px;
    height: 1200px;
  }

  /* Invitation card */
  .invitation {
    position: absolute;
    left: 20px;
    top: 364px;
    width: 670px;
    height: 672px;
    background: var(--paper);
    box-shadow: 0 2px 6px rgba(0,0,0,0.12);
    color: var(--ink);
  }
  .invitation__frame {
    position: absolute;
    left: 20px;
    top: 22px;
    width: 630px;
    height: 630px;
  }
  .invitation__text {
    position: absolute;
    left: 0;
    width: 100%;
    margin: 0;
    text-align: center;
    line-height: 1;
    font-variant-numeric: lining-nums;
  }
  .invitation__initials {
    top: 185px;
    font-family: "Playfair Display", serif;
    font-weight: 400;
    font-size: 52px;
    letter-spacing: 2px;
  }
  .invitation__lead {
    top: 373px;
    font-family: "Montserrat", sans-serif;
    font-size: 14px;
    letter-spacing: 1.6px;
  }
  .invitation__names {
    top: 398px;
    font-family: "Playfair Display", serif;
    font-weight: 400;
    font-size: 52px;
    letter-spacing: 3px;
  }
  .invitation__place {
    top: 462px;
    font-family: "Montserrat", sans-serif;
    font-size: 14px;
    letter-spacing: 1.6px;
  }
  .invitation__date {
    top: 486px;
    font-family: "Playfair Display", serif;
    font-size: 28px;
    letter-spacing: 4px;
  }
  .invitation__date small {
    font-size: 19px;
    letter-spacing: 1px;
  }
  .invitation__reception {
    top: 533px;
    font-family: "Playfair Display", serif;
    font-size: 13px;
    letter-spacing: 1.6px;
  }

  /* Logo card */
  .logo-card {
    position: absolute;
    left: 738px;
    top: 406px;
    width: 430px;
    height: 598px;
    background: var(--royal);
    box-shadow: 0 2px 6px rgba(0,0,0,0.15);
  }
  .logo-card__names {
    position: absolute;
    left: 0;
    top: 386px;
    width: 100%;
    margin: 0;
    text-align: center;
    font-family: "Bebas Neue", sans-serif;
    font-weight: 400;
    font-size: 50px;
    letter-spacing: 3px;
    color: var(--white);
    line-height: 1;
  }
</style>
</head>
<body>
<main class="canvas">

  <section class="invitation" aria-label="Wedding invitation">
    <svg class="invitation__frame" viewBox="0 0 630 630" aria-hidden="true">
      <rect x="1" y="1" width="628" height="628" fill="none" stroke="var(--ink)" stroke-width="2"/>
      <rect x="5" y="5" width="620" height="620" fill="none" stroke="var(--ink)" stroke-width="1"/>
      <rect x="10" y="10" width="610" height="610" fill="none" stroke="var(--ink)" stroke-width="7" stroke-dasharray="1 2"/>
      <rect x="15" y="15" width="600" height="600" fill="none" stroke="var(--ink)" stroke-width="1"/>
      <rect x="19" y="19" width="592" height="592" fill="none" stroke="var(--ink)" stroke-width="2"/>
    </svg>

    <p class="invitation__text invitation__initials">M &amp; C</p>
    <p class="invitation__text invitation__lead">YOU ARE INVITED! TO CELEBRATE THE WEDDING OF</p>
    <h1 class="invitation__text invitation__names">MARA &amp; COBB</h1>
    <p class="invitation__text invitation__place">AT CHARLOTTE, NORTH CAROLINA</p>
    <p class="invitation__text invitation__date">10 | 19 | 2019 | 4:30 <small>PM</small></p>
    <p class="invitation__text invitation__reception">RECEPTION TO FOLLOW</p>
  </section>

  <section class="logo-card" aria-label="Wedding logo card">
    <h2 class="logo-card__names">MARA &amp; COBB</h2>
  </section>

</main>
</body>
</html>
```